Lantern - Web Design Project

We are seeking to have our website redesigned. Our current webpage is rather dated looking www.lantern-outcomes.com We will be utilizing similar content to explain our services as what is in the website now. We do not see it at a retail portal but rather a website for those inquiring about our services as a reference check so to speak.

We wish to have a look that is considered clean, fresh, contemporary and contains a business savvy vibe.

We prefer isolated white background and also wish to retain the integrity of our Logo and colour scheme.

We are looking for something that doesnt look like it was designed at home on sitemoose. We are hoping to find something that looks like it would reside on a tablet.
Updates

Hello designers!

We apologize for our tardiness as we have been quite preoccupied. We will be extending our invites to the end of January!

Hello All,

Please review our offer once again for updated requirements.  We are hoping to accept a design by months end.

Lantern

Target Market(s)

Business to business clients and Large manufacturers

Industry/Entity Type

Retail

Requirements
Must have
• Existing Logo

There must be an area dedicated to an intro video that will be incorporated on our landing page.

We require design of the other pages as well not only the landing page.

```html
<!DOCTYPE html>
<html lang="en">
<head>
<meta charset="utf-8">
<title>Lantern Performance Group</title>
<link href="https://fonts.googleapis.com/css2?family=Arimo:wght@400;700&family=PT+Sans+Narrow:wght@400&family=Quicksand:wght@500;600&display=swap" rel="stylesheet">
<style>
  :root{
    --red:#c8141b;
    --red-dark:#a50f14;
    --text:#222;
    --muted:#555;
    --light:#777;
    --line:#dcdcdc;
    --nav-top:#ffffff;
    --nav-bottom:#dedede;
    --frame:#b0b0b0;
  }
  *{box-sizing:border-box;margin:0;padding:0}
  html,body{width:1200px;height:866px;overflow:hidden;background:#fff}
  body{font-family:"Arimo",Arial,sans-serif;color:var(--text);position:relative}
  .page{position:absolute;left:178px;top:0;width:849px;height:866px;border-left:1px solid var(--line);border-right:1px solid var(--line)}
  .abs{position:absolute}

  /* header */
  .brand{left:14px;top:14px}
  .brand-name{font-family:"Arimo",Arial,sans-serif;font-size:44px;font-weight:400;color:#555;letter-spacing:-1px;line-height:44px}
  .brand-tag{font-size:9px;color:#888;margin-left:16px;letter-spacing:.3px}
  .sign-in{right:9px;top:15px;font-size:11px;color:var(--muted);display:flex;align-items:center;gap:4px}
  .field{top:49px;height:26px;background:linear-gradient(#f1f1f1,#dcdcdc);border:1px solid #cfcfcf;font-size:10.5px;color:#666;padding:7px 10px;display:flex;justify-content:space-between;align-items:center}
  .language{left:607px;width:94px}
  .search{left:712px;width:128px}

  /* nav */
  .nav{left:0;top:92px;width:847px;height:54px;background:linear-gradient(var(--nav-top),var(--nav-bottom));border-top:1px solid var(--line);border-bottom:1px solid #cfcfcf;display:flex;align-items:center;padding-left:11px}
  .nav a{font-family:"PT Sans Narrow",Arial,sans-serif;font-size:15px;color:#444;text-decoration:none;padding:0 13px;height:31px;line-height:31px;border-right:1px solid #cfcfcf;text-transform:uppercase}
  .nav a.active{background:var(--red);color:#fff;padding:0 8px;margin-right:1px}

  /* slider */
  .slider{left:31px;top:159px;width:784px;height:264px;background:var(--frame);padding:8px 10px 9px}
  .slide{width:100%;height:100%;background:linear-gradient(100deg,#3a2314 0%,#b8683a 25%,#d9a060 40%,#7a7a28 52%,#1e3a2c 70%,#0d1a16 100%)}
  .slider-shadow{left:31px;top:423px;width:784px;height:30px;background:radial-gradient(ellipse at top,rgba(0,0,0,.18),rgba(0,0,0,0) 70%)}
  .dots{left:734px;top:391px;display:flex;gap:8px}
  .dots span{width:13px;height:13px;border-radius:50%;background:#1f2a26}
  .dots span.on{background:var(--red)}

  /* welcome */
  .welcome-title{left:34px;top:459px;font-family:"Quicksand",sans-serif;font-weight:600;font-size:21px;color:#444;letter-spacing:1px}
  .welcome-title em,.col-title em{font-style:normal;color:var(--red)}
  .welcome-text{left:33px;top:495px;width:528px;font-size:10.6px;line-height:15.3px;text-align:justify;color:var(--text)}
  .welcome-text p+p{margin-top:15.3px}
  .welcome-photo{left:584px;top:469px;width:219px;height:142px;border:1px solid #888;background:linear-gradient(160deg,#a8b0b2 0%,#6c7476 40%,#3d4244 100%)}
  .divider{left:32px;top:631px;width:786px;height:1px;background:var(--line)}

  /* columns */
  .col-title{top:653px;font-family:"Quicksand",sans-serif;font-weight:600;font-size:17px;color:#444;letter-spacing:1.2px;display:flex;align-items:center;gap:6px}
  .col-text{top:688px;width:241px;font-size:10.6px;line-height:15.3px;text-align:justify;color:#333}
  .read-more{top:753px;font-size:10.6px;color:var(--red);text-decoration:none}
  .read-more b{margin-left:6px}
  .clients{left:306px;top:690px;width:220px;display:grid;grid-template-columns:100px 120px;row-gap:14px}
  .client{font-family:"Arimo",Arial,sans-serif;font-size:19px;color:#8a8a8a;display:flex;align-items:center;gap:4px;height:24px}
  .client i{width:22px;height:22px;border-radius:50%;background:#9a9a9a;display:inline-block}

  /* footer */
  .footer-line{left:5px;top:809px;width:838px;height:1px;background:var(--line)}
  .footer-links{left:17px;top:823px;font-size:10.6px;color:var(--light)}
  .copyright{left:17px;top:842px;font-size:10.6px;color:var(--light)}
  .copyright a{color:var(--red-dark);text-decoration:none}
  .social{left:711px;top:825px;display:flex;gap:4px}
  .social span{width:22px;height:22px;display:block}
</style>
</head>
<body>
<div class="page">
  <header>
    <div class="abs brand">
      <div class="brand-name">Lantern</div>
      <div class="brand-tag">performance group</div>
    </div>
    <div class="abs sign-in">
      <svg width="14" height="14" viewBox="0 0 14 14"><circle cx="5" cy="5" r="3.5" fill="none" stroke="#777" stroke-width="1.5"/><path d="M7.5 7.5L12.5 12.5M10 10l1.5-1.5M11.5 11.5l1.3-1.3" stroke="#777" stroke-width="1.5"/></svg>
      Sign In
    </div>
    <div class="abs field language">Language
      <svg width="8" height="5" viewBox="0 0 8 5"><path d="M0 0h8L4 5z" fill="#666"/></svg>
    </div>
    <div class="abs field search">Search...
      <svg width="11" height="11" viewBox="0 0 11 11"><circle cx="6.5" cy="4.5" r="3.3" fill="none" stroke="#666" stroke-width="1.4"/><path d="M4 7L1 10" stroke="#666" stroke-width="1.6"/></svg>
    </div>
  </header>

  <nav class="abs nav">
    <a class="active" href="#">Home</a>
    <a href="#">Who We Are</a>
    <a href="#">Cross The Lantern</a>
    <a href="#">Performance Solutions</a>
    <a href="#">Sustain Solutions</a>
    <a href="#">Join Us</a>
  </nav>

  <section class="abs slider">
    <div class="slide" role="img" aria-label="Night photograph of a lit bridge walkway beside streaking traffic lights"></div>
  </section>
  <div class="abs slider-shadow"></div>
  <div class="abs dots"><span class="on"></span><span></span><span></span></div>

  <h1 class="abs welcome-title">Welcome to <em>Lantern Performance Group</em></h1>
  <div class="abs welcome-text">
    <p>Lantern Performance Group Inc. is the leading provider of profit generating and people development solutions. With the hands-on experience of best practices, the state-of-the-art technology and in-depth information we help companies increase their efficiencies and profits. Frank, honest, committed, valuable and rewarding are words that customers use to describe the quality services provided by Lantern Performance Group.</p>
    <p>Learn more about us, or find the right solutions for your specific business.We will be delighted to help you achieve better business results.</p>
  </div>
  <div class="abs welcome-photo" role="img" aria-label="Photograph of a curving coastal road with a guard rail"></div>

  <div class="abs divider"></div>

  <h2 class="abs col-title" style="left:32px">
    <svg width="28" height="28" viewBox="0 0 28 28"><circle cx="14" cy="14" r="12" fill="#8a9096"/><circle cx="14" cy="14" r="6" fill="#3d7fc4"/></svg>
    Our <em>Services</em></h2>
  <p class="abs col-text" style="left:32px">Neque porro quisquam est, qui dolorem ipsum quia dolor sit amet, consectetur, adipisci velit, sed quia non numquam eius modi tempora incidunt ut labore et dolore magnam aliquam quaerat.</p>
  <a class="abs read-more" href="#" style="left:242px">read more<b>»</b></a>

  <h2 class="abs col-title" style="left:308px">
    <svg width="28" height="28" viewBox="0 0 28 28"><circle cx="14" cy="14" r="12" fill="#c96a4a"/></svg>
    Our <em>Clients</em></h2>
  <div class="abs clients">
    <div class="client">Korvane</div>
    <div class="client" style="font-weight:700">Dextrel</div>
    <div class="client">Olvix</div>
    <div class="client"><i></i>Tidewell</div>
  </div>

  <h2 class="abs col-title" style="left:570px">
    <svg width="28" height="28" viewBox="0 0 28 28"><circle cx="14" cy="14" r="12" fill="#6d6d6d"/></svg>
    Who <em>we are</em></h2>
  <p class="abs col-text" style="left:569px">Qui dolorem ipsum quia dolor sit amet, consectetur, adipisci velit, sed quia non numquam eius modi tempora incidunt ut labore et dolore magnam aliquam quaerat.</p>
  <a class="abs read-more" href="#" style="left:747px">read more<b>»</b></a>

  <footer>
    <div class="abs footer-line"></div>
    <div class="abs footer-links">Home | Who We Are | Cross The Lantern | Performance Solutions | Sustain Solutions | Join Us</div>
    <div class="abs copyright">© Copyright 2012 &nbsp;|&nbsp; <a href="#">Lantern Performance Group</a> &nbsp;|&nbsp; All rights reserved.</div>
    <div class="abs social" aria-label="Social links">
      <span style="background:#3b5998"></span>
      <span style="background:#d34836"></span>
      <span style="background:#1c87bd"></span>
      <span style="background:#2fa9e0"></span>
      <span style="background:#c4302b"></span>
    </div>
  </footer>
</div>
</body>
</html>
```